Dorian Felsgrove breaking. Or D. Felsgrove breaking

I break in and train horses, any age any bread of horse, for any disaplin. I need a business card that is simple but effective, in the way of looking professional. I would like a horse on my card, preferably a horse without a rider. I also pre train horse, younge horses that need a bit of riding before they go into serious work, and prepare yearlings for sale.

Reason: This is for my boyfriend, and I really want it to be perfect and impressive!

Target Market(s)

Thoroughbred race horse trainers, horse industrie people.

Industry/Entity Type

Business

Contact Information for Business Card

Dorian Felsgrove horse breaking, "WOLBUNDA" Armidale, give your horse the right start to any career. dfels@quillmail.com.au, 0431862097. Horse breaking~pre-training~sale preparation

```html
<!DOCTYPE html>
<html lang="en">
<head>
<meta charset="utf-8">
<title>Dorian Felsgrove horse breaking</title>
<link href="https://fonts.googleapis.com/css2?family=Bodoni+Moda:opsz,wght@6..96,400;6..96,500&display=swap" rel="stylesheet">
<style>
  :root {
    --ink: #ffffff;
    --rule: rgba(255, 255, 255, 0.45);
    --shade: rgba(20, 22, 20, 0.55);
    --turf: #4f6e3a;
    --dirt: #5a4a3a;
    --gate: #5c6168;
    --silk: #2e3f7a;
  }
  * { margin: 0; padding: 0; box-sizing: border-box; }
  html, body {
    width: 1200px;
    height: 741px;
    overflow: hidden;
    background: #1d1f1d;
  }
  .card {
    position: relative;
    width: 1200px;
    height: 741px;
    overflow: hidden;
    font-family: "Bodoni Moda", "Didot", serif;
    color: var(--ink);
  }
  .race-photo {
    position: absolute;
    inset: 0;
    background:
      linear-gradient(var(--shade), var(--shade)),
      radial-gradient(ellipse 380px 260px at 650px 330px, var(--silk) 0%, transparent 70%),
      linear-gradient(90deg, var(--gate) 0%, #3a3d40 30%, transparent 55%),
      linear-gradient(180deg, var(--turf) 0%, #3d5a2c 35%, var(--dirt) 70%, #4a3c30 100%);
  }
  .line {
    position: absolute;
    left: 0;
    width: 100%;
    text-align: center;
    line-height: 1;
    white-space: nowrap;
    font-weight: 400;
  }
  .strapline  { top: 38px;  font-size: 41px; }
  .name       { top: 114px; font-size: 92px; }
  .trade      { top: 220px; font-size: 92px; }
  .location   { top: 350px; font-size: 43px; }
  .email      { top: 421px; font-size: 74px; }
  .phone      { top: 514px; font-size: 76px; }
  .services   { top: 627px; font-size: 35px; }
  .base-rule {
    position: absolute;
    left: 0;
    top: 699px;
    width: 100%;
    height: 1px;
    background: var(--rule);
  }
</style>
</head>
<body>
  <main class="card">
    <div class="race-photo" role="img" aria-label="Racehorses with jockeys breaking from the starting gates on a dirt track, darkened"></div>
    <p class="line strapline">Give your horse the right start to any career</p>
    <h1 class="line name">Dorian Felsgrove</h1>
    <h2 class="line trade">horse breaking</h2>
    <p class="line location">"WOLBUNDA" Armidale</p>
    <p class="line email">dfels@quillmail.com.au</p>
    <p class="line phone">0431862097</p>
    <p class="line services">Horse breaking~pre-training~sale preparation</p>
    <div class="base-rule"></div>
  </main>
</body>
</html>
```